Verdant Pathworks Business Card

want the back of card to be blue- with the logo in the center
front of card- info plus logo (info being mailing address, email address, and website address )
4 different names with titles to have on cards
1) Dominic Ashvale - Owner
2) Bethany Korvuth- Customer Relationship Specialist
3) Luca Brennwick- Vice President of Sales
4) Neil Umbright- Chief Technology Officer

Target Market(s)

tech company in the government/probation office industry

Industry/Entity Type

Government Office

Contact Information for Business Card

1) Dominic Ashvale - Owner

Colors
0355a3
ffffff

Requirements
Must have
• back side should be blue, with the logo placed in the center
• front side needs to include both the logo, as well as company info (info should include website address, email address, and mailing address)

```html
<!DOCTYPE html>
<html lang="en">
<head>
<meta charset="UTF-8">
<title>Verdant Pathworks Business Card</title>
<link rel="stylesheet" href="https://fonts.googleapis.com/css2?family=Cinzel:wght@600&family=Raleway:wght@400;500&display=swap">
<style>
  :root {
    --navy: #142d55;
    --grey: #808285;
    --white: #ffffff;
    --canvas: #dcdcdc;
    --ink-soft: #6d6e71;
  }
  * { margin: 0; padding: 0; box-sizing: border-box; }
  html, body {
    width: 1200px; height: 1200px; overflow: hidden;
    background: var(--canvas);
  }
  .card-spread {
    position: absolute; left: 60px; top: 442px;
    width: 1080px; height: 315px; display: flex;
  }
  .card { position: relative; width: 540px; height: 315px; overflow: hidden; }

  /* back side */
  .card-back { background: var(--navy); }
  .back-brand {
    position: absolute; left: 0; right: 0; top: 112px;
    display: flex; flex-direction: column; align-items: center; gap: 14px;
  }
  .brand-dot {
    width: 34px; height: 34px; border-radius: 50%;
    background: var(--white);
  }
  .brand-name {
    font-family: "Cinzel", serif; font-weight: 600;
    font-size: 30px; letter-spacing: 1px; line-height: 1;
    color: var(--white); text-align: center;
  }
  .back-stripe {
    position: absolute; left: 0; right: 0; top: 248px; height: 22px;
    background: var(--grey);
    font-family: "Raleway", sans-serif; font-size: 12px; font-weight: 500;
    letter-spacing: 3.2px; color: var(--white);
    display: flex; align-items: center; justify-content: center;
  }

  /* front side */
  .card-front { background: var(--white); }
  .front-brand {
    position: absolute; left: 32px; top: 32px;
    font-family: "Cinzel", serif; font-weight: 600;
    font-size: 22px; line-height: 1.15; letter-spacing: 1px;
    color: var(--navy);
  }
  .front-mark {
    position: absolute; left: 346px; top: 42px;
    width: 156px; height: 156px; border-radius: 50%;
    border: 7px solid var(--navy);
  }
  .person {
    position: absolute; left: 28px; top: 144px;
    border-left: 5px solid var(--navy); padding-left: 6px;
    font-family: "Raleway", sans-serif;
  }
  .person-name { font-size: 23px; font-weight: 500; color: var(--navy); line-height: 1.05; }
  .person-title { font-size: 14px; color: var(--ink-soft); letter-spacing: .5px; }
  .address {
    position: absolute; left: 37px; top: 225px;
    font-family: "Raleway", sans-serif; font-size: 14px; color: var(--ink-soft);
  }
  .contact-band {
    position: absolute; left: 0; right: 0; top: 248px; bottom: 0;
    background: var(--navy); padding: 8px 0 0 37px;
    display: grid; grid-template-columns: 135px auto; row-gap: 3px;
    font-family: "Raleway", sans-serif; font-size: 13px; color: var(--white);
  }
  .contact-item { display: flex; align-items: center; gap: 3px; white-space: nowrap; }
  .contact-item svg { width: 10px; height: 10px; fill: var(--white); }
</style>
</head>
<body>
  <main class="card-spread">
    <section class="card card-back" aria-label="Card back">
      <div class="back-brand">
        <span class="brand-dot"></span>
        <span class="brand-name">Verdant Pathworks</span>
      </div>
      <div class="back-stripe">www.verdantpathworks.net</div>
    </section>

    <section class="card card-front" aria-label="Card front">
      <div class="front-brand">Verdant<br>Pathworks</div>
      <div class="front-mark"></div>

      <div class="person">
        <div class="person-name">Dominic Ashvale</div>
        <div class="person-title">OWNER</div>
      </div>

      <div class="address">Your Full Address Comes here</div>

      <div class="contact-band">
        <span class="contact-item">
          <svg viewBox="0 0 10 10"><path d="M2 0.5 L3.6 2.6 L2.8 3.6 Q4 5.8 6.4 7.2 L7.4 6.4 L9.5 8 L8.2 9.6 Q3.2 8.6 0.4 1.8 Z"/></svg>
          : (000) 000-0000
        </span>
        <span class="contact-item">
          <svg viewBox="0 0 10 10"><rect x="2.5" y="0.5" width="5" height="3"/><rect x="0.5" y="3.5" width="9" height="4" rx="1"/><rect x="2.5" y="6.5" width="5" height="3"/></svg>
          : (000) 000-0000
        </span>
        <span class="contact-item">
          <svg viewBox="0 0 10 10"><path d="M2.5 0.5 H7.5 V9.5 H2.5 Z M3.5 1.5 V7.5 H6.5 V1.5 Z"/></svg>
          : (000) 000-0000
        </span>
        <span class="contact-item">
          <svg viewBox="0 0 10 10"><path d="M0.5 2 H9.5 V8 H0.5 Z M1.2 2.6 L5 5.6 L8.8 2.6 Z" fill-rule="evenodd"/></svg>
          : info@verdantpathworks.net
        </span>
      </div>
    </section>
  </main>
</body>
</html>
```